Film and TV production company

I have the logo already designed by craft nest. I just need the text and the logo attached to the business card. Maybe a small design on the back of the card or text.

Industry/Entity Type

film tv arts

Contact Information for Business Card

Brent Walcott Cinematographer-Director

Colors
F0912C
F2A743
F7CA91
FBE8D2
FDF5EE
EE7325
F08F49
F5BC92
FAE3D3
FDF4ED

Requirements
Must have
• www.bluewattlestudio.com.au my email address mail@bluewattlestudio.com.au my mobile number 0412573984
Nice to have
• Some kind of small art work on the back that ties in with the logo design attached
Should not have
• Must clean and simple

```html
<!DOCTYPE html>
<html lang="en">
<head>
<meta charset="utf-8">
<title>Blue Wattle Studio – Business Card</title>
<link href="https://fonts.googleapis.com/css2?family=Lato:wght@400;700&display=swap" rel="stylesheet">
<style>
  :root {
    --page: #eceeef;
    --card-front: #ffffff;
    --card-back: #1e1e1e;
    --card-back-glow: #2a2a2a;
    --ink: #1f1f1f;
    --muted: #4a4a4a;
    --accent: #ee7325;
    --accent-soft: #f08f49;
    --divider: #c9c9c9;
    --back-text: #ffffff;
  }
  * { box-sizing: border-box; margin: 0; padding: 0; }
  html, body {
    width: 1047px; height: 1200px; overflow: hidden;
    background: var(--page);
    font-family: "Lato", Arial, sans-serif;
  }
  .card {
    position: absolute;
    left: 160px;
    width: 740px; height: 424px;
    border-radius: 24px;
    overflow: hidden;
    box-shadow: 0 4px 12px rgba(0,0,0,0.18);
  }
  .card--front { top: 120px; background: var(--card-front); }
  .card--back { top: 634px; background: var(--card-back); }

  .brand {
    position: absolute;
    display: flex; flex-direction: column; align-items: center;
  }
  .brand__dot {
    border-radius: 50%;
    background: var(--accent);
  }
  .brand__name {
    font-weight: 400;
    white-space: nowrap;
    text-transform: uppercase;
  }
  .card--front .brand { left: 40px; width: 380px; top: 130px; }
  .card--front .brand__dot { width: 108px; height: 108px; margin-bottom: 16px; }
  .card--front .brand__name { font-size: 19px; letter-spacing: 0.14em; color: var(--ink); }

  .divider {
    position: absolute; left: 384px; top: 130px;
    width: 1px; height: 180px; background: var(--divider);
  }

  .contact { position: absolute; left: 420px; top: 136px; }
  .contact__name {
    font-size: 32px; font-weight: 400; color: var(--ink);
    letter-spacing: 0.02em; text-transform: uppercase; line-height: 1.2;
  }
  .contact__role { font-size: 18px; color: var(--accent-soft); margin-top: 2px; }
  .contact__list { list-style: none; margin-top: 22px; }
  .contact__item {
    display: flex; align-items: center; gap: 12px;
    font-size: 17px; color: var(--muted); letter-spacing: 0.03em;
    height: 28px;
  }
  .contact__icon { width: 14px; height: 14px; fill: var(--accent); flex: none; }

  .back-texture {
    position: absolute; inset: 0;
    background: radial-gradient(ellipse at 50% 45%, var(--card-back-glow) 0%, var(--card-back) 70%);
  }
  .card--back .brand { left: 0; width: 740px; top: 96px; }
  .card--back .brand__dot { width: 170px; height: 170px; margin-bottom: 22px; }
  .card--back .brand__name { font-size: 34px; letter-spacing: 0.14em; color: var(--back-text); }
</style>
</head>
<body>

<section class="card card--front">
  <div class="brand">
    <div class="brand__dot"></div>
    <div class="brand__name">Blue Wattle Studio</div>
  </div>

  <div class="divider"></div>

  <div class="contact">
    <h1 class="contact__name">Brent Walcott</h1>
    <p class="contact__role">Cinematographer-Director</p>
    <ul class="contact__list">
      <li class="contact__item">
        <svg class="contact__icon" viewBox="0 0 24 24"><path d="M6.6 10.8a15.1 15.1 0 0 0 6.6 6.6l2.2-2.2a1 1 0 0 1 1-.25 11.4 11.4 0 0 0 3.6.57 1 1 0 0 1 1 1V20a1 1 0 0 1-1 1A17 17 0 0 1 3 4a1 1 0 0 1 1-1h3.5a1 1 0 0 1 1 1c0 1.25.2 2.45.57 3.57a1 1 0 0 1-.25 1z"/></svg>
        0412573984
      </li>
      <li class="contact__item">
        <svg class="contact__icon" viewBox="0 0 24 24"><path d="M2 5h20v2l-10 6L2 7zM2 9l10 6 10-6v10H2z"/></svg>
        mail@bluewattlestudio.com.au
      </li>
      <li class="contact__item">
        <svg class="contact__icon" viewBox="0 0 24 24"><circle cx="12" cy="12" r="10"/></svg>
        bluewattlestudio.com.au
      </li>
    </ul>
  </div>
</section>

<section class="card card--back">
  <div class="back-texture" role="img" aria-label="Subtle dark background texture"></div>
  <div class="brand">
    <div class="brand__dot"></div>
    <div class="brand__name">Blue Wattle Studio</div>
  </div>
</section>

</body>
</html>
```